Business Card Design - Local Loss Adjusting Office

Please read the description! We will provide an example of one concept with all required information that needs organization. Other concepts has to be your own design. We would require icons - if it fits the design - instead of letters when it comes to Telephone, Mobile, Fax, etc. The design has to be elegant, modern, and simple. We need the Photoshop/Illustrator files in latest version with layers. We would require a PDF of the cards as well a JPG version. The font used should be Calibri. The colors are included in the first concept sample attached. The name - the person name only that is - should be put in duplicate because we will use another language in one of the lines The card size is 5.5cm x 8.5cm. If you need anything else, please let us know. Thank you.
Reason: Most designers haven't read the project description properly!
Hi All,
We need to choose one design tomorrow, and would like to bring to your attention the following:
1- We are Velorin Adjusting not Dorian Whitfield! We are exclusive local representative of Dorian Whitfield. This should only be on the back side of the card.
2- We will use bilingual names for employees. Therefore put a duplicate English name, we will change one to another language with our in house designer afterwards.
3- All icons should be on the left side of text never on the right.
4- Don't change the logo colors please.
5- Dont overcrowd the card with colors. Simple, elegant, and modern please.
Sorry for not being able to respond to all inquires as we have 100+ submissions.
Goodluck to all.
Best regards,
Velorin

```html
<!DOCTYPE html>
<html lang="en">
<head>
<meta charset="utf-8">
<title>Velorin Adjusting — Business Card</title>
<link href="https://fonts.googleapis.com/css2?family=Carlito:wght@400;700&display=swap" rel="stylesheet">
<style>
  :root {
    --page: #e9e7e3;
    --card: #ffffff;
    --card-shade: #f1f1f1;
    --ink: #5a5a5a;
    --ink-dark: #3d3d3d;
    --green: #9ccc3c;
    --green-soft: #b5d96a;
    --band: #3a3b3d;
    --band-light: #4a4b4e;
    --band-text: #f2f2f2;
    --partner-blue: #2a8fcf;
  }
  * { margin: 0; padding: 0; box-sizing: border-box; }
  html, body { width: 1200px; height: 1023px; overflow: hidden; }
  body {
    background: var(--page);
    font-family: "Carlito", "Calibri", sans-serif;
    color: var(--ink);
    display: flex;
    align-items: center;
    justify-content: center;
    gap: 40px;
  }
  .card {
    position: relative;
    width: 540px;
    height: 350px;
    background: linear-gradient(180deg, var(--card) 0%, var(--card-shade) 100%);
    box-shadow: 0 2px 4px rgba(0,0,0,.12), 0 10px 24px rgba(0,0,0,.12);
    overflow: hidden;
  }

  /* Front */
  .brand {
    position: absolute;
    right: 40px;
    top: 34px;
    text-align: right;
    color: var(--ink);
    font-weight: 700;
    line-height: .9;
  }
  .brand .brand-name { font-size: 54px; letter-spacing: -1px; display: block; }
  .brand .brand-sub { font-size: 24px; display: block; }
  .accent-line {
    position: absolute;
    left: 0; top: 130px;
    width: 100%; height: 3px;
    background: var(--green-soft);
  }
  .accent-bar {
    position: absolute;
    left: 0; top: 124px;
    width: 300px; height: 9px;
    background: var(--green);
  }
  .people {
    position: absolute;
    left: 34px; top: 150px;
  }
  .person { margin-bottom: 8px; }
  .person-name { font-size: 19px; color: var(--green); }
  .person-name .creds { font-size: 12px; color: var(--ink); }
  .person-role { font-size: 13px; color: var(--ink); }

  .contact-band {
    position: absolute;
    left: 0; bottom: 0;
    width: 100%; height: 98px;
    background: linear-gradient(180deg, var(--band-light), var(--band));
    border-top: 2px solid var(--green);
    display: flex;
    gap: 44px;
    padding: 16px 34px 0;
  }
  .contact-list { list-style: none; }
  .contact-list li {
    display: flex;
    align-items: center;
    gap: 8px;
    color: var(--band-text);
    font-size: 13.5px;
    margin-bottom: 6px;
  }
  .icon { width: 14px; height: 14px; flex: none; }

  /* Back */
  .back-brand {
    position: absolute;
    left: 0; right: 0; top: 110px;
    text-align: center;
    color: var(--ink);
    font-weight: 700;
    line-height: .9;
  }
  .back-brand .brand-name { font-size: 72px; letter-spacing: -1px; display: block; }
  .back-brand .brand-sub { font-size: 30px; display: block; }
  .representation {
    position: absolute;
    left: 40px; bottom: 36px;
    display: flex;
    align-items: center;
    gap: 12px;
  }
  .representation-label {
    font-size: 12px;
    letter-spacing: .5px;
    color: var(--ink-dark);
    line-height: 1.2;
  }
  .representation-divider { width: 1px; height: 34px; background: var(--partner-blue); }
  .partner-name { font-size: 18px; color: var(--partner-blue); }
  .web-address {
    position: absolute;
    left: 14px; top: 50%;
    transform: translateY(-50%) rotate(-90deg);
    transform-origin: left center;
    font-size: 12px;
    font-weight: 700;
    color: var(--ink-dark);
    white-space: nowrap;
  }
</style>
</head>
<body>

<section class="card card-front" aria-label="Card front">
  <div class="brand">
    <span class="brand-name">velorin adjusting</span>
  </div>
  <div class="accent-line"></div>
  <div class="accent-bar"></div>

  <div class="people">
    <div class="person">
      <div class="person-name">Karim S. AlHaddad <span class="creds">- C.Eng., A.M.ASCE, MBA, FCII</span></div>
      <div class="person-role">Licensed Loss Adjuster &amp; Managing Partner</div>
    </div>
    <div class="person">
      <div class="person-name">Karim S. AlHaddad <span class="creds">- C.Eng., A.M.ASCE, MBA, FCII</span></div>
      <div class="person-role">Licensed Loss Adjuster &amp; Managing Partner</div>
    </div>
  </div>

  <div class="contact-band">
    <ul class="contact-list">
      <li>
        <svg class="icon" viewBox="0 0 14 14" aria-hidden="true"><rect width="14" height="14" rx="2" fill="#9ccc3c"/><rect x="4.5" y="2.5" width="5" height="9" rx="1" fill="none" stroke="#3a3b3d" stroke-width="1.2"/><circle cx="7" cy="10" r=".6" fill="#3a3b3d"/></svg>
        +(965) 90471258
      </li>
      <li>
        <svg class="icon" viewBox="0 0 14 14" aria-hidden="true"><rect width="14" height="14" rx="2" fill="#9ccc3c"/><rect x="4.5" y="2.5" width="5" height="9" rx="1" fill="none" stroke="#3a3b3d" stroke-width="1.2"/><circle cx="7" cy="10" r=".6" fill="#3a3b3d"/></svg>
        +(971) 552086731
      </li>
      <li>
        <svg class="icon" viewBox="0 0 14 14" aria-hidden="true"><rect width="14" height="14" rx="2" fill="#9ccc3c"/><rect x="3" y="4" width="8" height="6" fill="none" stroke="#3a3b3d" stroke-width="1.2"/><path d="M3 4l4 3 4-3" fill="none" stroke="#3a3b3d" stroke-width="1.2"/></svg>
        karim@velorin.com
      </li>
    </ul>
    <ul class="contact-list">
      <li>
        <svg class="icon" viewBox="0 0 14 14" aria-hidden="true"><rect width="14" height="14" rx="2" fill="#9ccc3c"/><path d="M4 3.5c-.8.8-.6 2.6 1.6 4.8s4 2.4 4.8 1.6l.6-.8-1.8-1.4-.9.7c-.7-.3-1.9-1.5-2.2-2.2l.7-.9L5.4 3.5z" fill="#3a3b3d"/></svg>
        +(965) 22317604
      </li>
      <li>
        <svg class="icon" viewBox="0 0 14 14" aria-hidden="true"><rect width="14" height="14" rx="2" fill="#9ccc3c"/><rect x="3" y="6" width="8" height="5" fill="#3a3b3d"/><rect x="4.5" y="3" width="5" height="3" fill="none" stroke="#3a3b3d" stroke-width="1"/></svg>
        +(965) 25469213
      </li>
      <li>
        <svg class="icon" viewBox="0 0 14 14" aria-hidden="true"><rect width="14" height="14" rx="2" fill="#9ccc3c"/><path d="M7 2.5a3 3 0 0 0-3 3c0 2.2 3 6 3 6s3-3.8 3-6a3 3 0 0 0-3-3z" fill="#3a3b3d"/><circle cx="7" cy="5.5" r="1" fill="#9ccc3c"/></svg>
        P.O. Box 2750 Safat, Kuwait 13088
      </li>
    </ul>
  </div>
</section>

<section class="card card-back" aria-label="Card back">
  <div class="web-address">www.velorin.com</div>
  <div class="back-brand">
    <span class="brand-name">velorin adjusting</span>
  </div>
  <div class="representation">
    <div class="representation-label">EXCLUSIVE LOCAL<br>REPRESENTITIVE OF</div>
    <div class="representation-divider"></div>
    <div class="partner-name">Dorian Whitfield</div>
  </div>
</section>

</body>
</html>
```